Beacon Law Stationary - Law Firm

I am looking for a designer who can help me design letterhead and envelopes consistent with our new business cards. Feel free to reach out to me directly at ned@beaconlawgroup.example. Thank you!! Visit beaconlawgroup.example to see our site and the attached files for creative assets.

Target Market(s)

Anyone needing a lawyer

Font styles to use
Other font styles liked:
• Adobe Caslon Pro

Requirements
Must have
• Adobe Caslon Pro font
Full color
Nice to have
• My photo on front along with 2/3 face of camo - see mock up for example of what I have in mind.

American colors - similar to the ones found on my website and gold.

```html
<!DOCTYPE html>
<html lang="en">
<head>
<meta charset="utf-8">
<title>Beacon Law Stationery</title>
<link href="https://fonts.googleapis.com/css2?family=Libre+Caslon+Text:wght@400;700&family=Montserrat:wght@300;400&family=Tinos&display=swap" rel="stylesheet">
<style>
  :root {
    --navy: #0e2647;
    --gold: #b09a5e;
    --paper: #ffffff;
    --backdrop: #b9d0e6;
    --ink: #2a2a2a;
    --muted: #8a8a8a;
  }
  * { margin: 0; padding: 0; box-sizing: border-box; }
  html, body { width: 1200px; height: 1200px; overflow: hidden; }
  body { background: var(--backdrop); position: relative; font-family: "Montserrat", sans-serif; }

  .sheet { position: absolute; background: var(--paper); overflow: hidden; }
  .footer-band {
    position: absolute; left: 0; bottom: 0; width: 100%;
    background: linear-gradient(170deg, var(--paper) 0%, var(--paper) 30%, var(--gold) 55%, var(--navy) 75%);
  }

  /* Letterhead */
  .letterhead { left: 77px; top: 265px; width: 460px; height: 650px; }
  .letterhead .masthead { height: 74px; background: var(--navy); position: relative; }
  .wordmark {
    font-family: "Libre Caslon Text", serif; color: var(--gold);
    text-transform: uppercase; letter-spacing: 0.5px; white-space: nowrap;
  }
  .letterhead .wordmark { position: absolute; left: 53px; top: 28px; font-size: 15px; }
  .contact-block {
    position: absolute; left: 336px; top: 12px; padding-left: 8px;
    border-left: 1px solid var(--gold);
    font-family: "Tinos", serif; color: #fff; font-size: 7px; line-height: 9px;
    white-space: nowrap;
  }
  .contact-block .row { display: flex; align-items: center; gap: 4px; }
  .contact-block .row svg { width: 6px; height: 6px; fill: var(--gold); }
  .contact-block .address { margin-top: 5px; }

  .letter { position: absolute; left: 47px; top: 145px; width: 367px; }
  .letter .to { font-size: 7.5px; letter-spacing: 1px; color: var(--ink); }
  .letter .date { position: absolute; right: 0; top: 0; font-size: 6px; color: #555; }
  .recipient-name { font-size: 7px; color: var(--gold); margin-top: 5px; }
  .recipient-lines { font-size: 5.5px; color: var(--muted); line-height: 10px; margin-top: 2px; }
  .body-copy { margin-top: 22px; font-size: 5.6px; line-height: 8px; color: #8d8d8d; font-weight: 300; text-align: justify; }
  .body-copy p { margin-bottom: 8px; }
  .signature-mark { width: 80px; height: 18px; background: #e6e6e6; margin-top: 36px; border-radius: 2px; }
  .signer { font-size: 7px; color: var(--ink); margin-top: 6px; }
  .signer-title { font-size: 5.5px; color: var(--muted); }
  .letterhead .footer-band { height: 60px; }

  /* Envelope front */
  .envelope-front { left: 574px; top: 310px; width: 549px; height: 240px; }
  .envelope-front .masthead { height: 77px; background: var(--navy); position: relative; }
  .envelope-front .wordmark { position: absolute; left: 48px; top: 27px; font-size: 15.5px; }
  .envelope-front .return-address {
    position: absolute; left: 48px; top: 49px;
    font-family: "Tinos", serif; color: #fff; font-size: 7px; line-height: 9.5px;
  }
  .envelope-front .footer-band { height: 70px; }

  /* Envelope back */
  .envelope-back { left: 574px; top: 626px; width: 549px; height: 238px; }
  .envelope-back .flap { position: absolute; left: 0; top: 0; }
  .envelope-back .wordmark { position: absolute; left: 0; width: 549px; text-align: center; top: 25px; font-size: 13px; }
</style>
</head>
<body>

<section class="sheet letterhead" aria-label="Letterhead">
  <header class="masthead">
    <div class="wordmark">Beacon Law</div>
    <div class="contact-block">
      <div class="row"><svg viewBox="0 0 10 10"><path d="M2 0 L4 2.5 L3 3.5 Q4.5 6 6.5 7 L7.5 6 L10 8 L8.5 10 Q2 9 0 1.5 Z"/></svg>407 555 0142</div>
      <div class="row"><svg viewBox="0 0 10 10"><path d="M0 2 H10 V8 H0 Z M0.8 2.6 L5 5.6 L9.2 2.6" fill="none" stroke="#b09a5e" stroke-width="1.2"/></svg>ned@beaconlawgroup.example</div>
      <div class="row"><svg viewBox="0 0 10 10"><circle cx="5" cy="5" r="4.5"/></svg>beaconlawgroup.example</div>
      <div class="address">214 Maple Court<br>Street Riverton, Ohio 44210</div>
    </div>
  </header>

  <div class="letter">
    <div class="to">TO</div>
    <div class="date">Friday, 01/01/2018</div>
    <div class="recipient-name">Dana Whitfield</div>
    <div class="recipient-lines">Human Resources<br>Northgate Inc.<br>1105-D Elm Row, Westfield<br>E89 USA</div>
    <div class="body-copy">
      <p>We write to confirm receipt of your recent inquiry and to outline the next steps in our review. Our team has gathered the relevant records and will prepare a short summary of the key issues for your consideration. Please review the enclosed notes and share any questions before our scheduled meeting next week.</p>
      <p>We appreciate your patience as we complete this process and look forward to working with you.</p>
      <p>All materials remain strictly confidential.</p>
      <p>Our attorneys will contact you shortly to arrange a convenient time for a full consultation. During that call we will discuss the timeline, expected costs and any documents still required to move your matter forward without delay.</p>
      <p>If anything changes in the meantime, please let us know at once so we can update our plan. We remain committed to clear communication and careful, thorough work on every case we accept.</p>
      <p>Thank you again for choosing our firm.</p>
    </div>
    <div class="signature-mark" role="img" aria-label="Handwritten signature"></div>
    <div class="signer">Paul Reyes</div>
    <div class="signer-title">Managing Director</div>
  </div>

  <div class="footer-band" role="img" aria-label="Decorative navy and gold footer wave"></div>
</section>

<section class="sheet envelope-front" aria-label="Envelope front">
  <header class="masthead">
    <div class="wordmark">Beacon Law</div>
    <div class="return-address">214 Maple Court<br>Street Riverton, Ohio 44210</div>
  </header>
  <div class="footer-band" role="img" aria-label="Decorative navy and gold footer wave"></div>
</section>

<section class="sheet envelope-back" aria-label="Envelope back">
  <svg class="flap" width="549" height="70" viewBox="0 0 549 70">
    <path d="M0 0 L549 0 L540 40 Q534 65 510 65 L40 65 Q16 65 12 45 Z" fill="var(--navy)"/>
  </svg>
  <div class="wordmark">Beacon Law</div>
</section>

</body>
</html>
```